Pemberton Dialworks Business Card Design

Double Sided Business Card Design for a Locksmith company specializing in Safecracking, safe & vault service.

```html
<!DOCTYPE html>
<html lang="en">
<head>
<meta charset="utf-8">
<title>Pemberton Dialworks – Business Card</title>
<link rel="stylesheet" href="https://fonts.googleapis.com/css2?family=Montserrat:wght@400;500;600;800&display=swap">
<style>
  :root {
    --brand-green: #2f7d45;
    --brand-green-dark: #246437;
    --card-white: #f7f7f7;
    --ink: #1e1e1e;
    --backdrop: #d9d9d9;
  }
  * { margin: 0; padding: 0; box-sizing: border-box; }
  html, body { width: 1200px; height: 675px; overflow: hidden; }
  body {
    background: var(--backdrop);
    font-family: "Montserrat", sans-serif;
    display: flex;
    align-items: center;
    justify-content: center;
    gap: 60px;
  }
  .card {
    position: relative;
    width: 520px;
    height: 297px;
    border-radius: 16px;
    overflow: hidden;
    box-shadow: 0 10px 24px rgba(0,0,0,0.18);
  }

  /* Front */
  .card--front { background: var(--card-white); }
  .front-panel { position: absolute; inset: 0; }
  .brand-lockup {
    position: absolute;
    left: 22px;
    top: 176px;
    display: flex;
    align-items: center;
    gap: 8px;
  }
  .brand-dot {
    width: 30px; height: 30px;
    border-radius: 50%;
    background: var(--brand-green);
    flex: none;
  }
  .brand-name {
    font-weight: 800;
    font-size: 17px;
    line-height: 1.05;
    color: var(--ink);
    text-transform: uppercase;
    letter-spacing: 0.5px;
    background: var(--card-white);
    padding: 2px 4px;
  }
  .contact-block {
    position: absolute;
    left: 300px;
    top: 92px;
    width: 196px;
  }
  .person-name {
    font-weight: 600;
    font-size: 21px;
    color: var(--brand-green);
    letter-spacing: 0.5px;
  }
  .person-role {
    font-size: 10px;
    color: var(--ink);
    margin-left: 4px;
    margin-top: -2px;
  }
  .divider {
    height: 2px;
    background: var(--brand-green);
    margin: 10px 0 10px;
  }
  .contact-list { list-style: none; }
  .contact-item {
    display: flex;
    align-items: flex-start;
    gap: 7px;
    font-size: 10.5px;
    line-height: 1.4;
    color: var(--ink);
    margin-bottom: 3px;
  }
  .contact-icon { width: 10px; height: 10px; flex: none; margin-top: 3px; fill: var(--brand-green); }

  /* Back */
  .card--back {
    background: var(--brand-green);
    display: flex;
    align-items: center;
    justify-content: center;
  }
  .back-lockup { display: flex; align-items: center; gap: 14px; }
  .back-dot { width: 64px; height: 64px; border-radius: 50%; background: #ffffff; flex: none; }
  .back-name {
    font-weight: 800;
    font-size: 30px;
    line-height: 1.05;
    color: #ffffff;
    text-transform: uppercase;
    letter-spacing: 1px;
  }
</style>
</head>
<body>

  <section class="card card--front" aria-label="Card front">
    <svg class="front-panel" viewBox="0 0 520 297" width="520" height="297" role="img" aria-label="Green curved brand panel">
      <path d="M150 0 H200 A190 190 0 0 1 215 297 H150 Z" fill="var(--brand-green)"/>
      <path d="M200 0 A190 190 0 0 1 215 297 H240 A200 200 0 0 0 250 0 Z" fill="var(--brand-green)" opacity="0"/>
    </svg>

    <div class="brand-lockup">
      <span class="brand-dot"></span>
      <span class="brand-name">Pemberton<br>Dialworks</span>
    </div>

    <div class="contact-block">
      <h2 class="person-name">NAME</h2>
      <p class="person-role">Designation</p>
      <div class="divider"></div>
      <ul class="contact-list">
        <li class="contact-item">
          <svg class="contact-icon" viewBox="0 0 10 10"><path d="M5 0a3.5 3.5 0 0 0-3.5 3.5C1.5 6 5 10 5 10s3.5-4 3.5-6.5A3.5 3.5 0 0 0 5 0zm0 5a1.4 1.4 0 1 1 0-2.8A1.4 1.4 0 0 1 5 5z"/></svg>
          <span>5820 Harlow Ave,<br>Suite 310, Pemberton, TX 75044</span>
        </li>
        <li class="contact-item">
          <svg class="contact-icon" viewBox="0 0 10 10"><path d="M2 0.5l1.8 2-1 1.2a6 6 0 0 0 3.5 3.5l1.2-1 2 1.8-1 1.5C4.5 9.5 0.5 5.5 0.5 1.5z"/></svg>
          <span>555-214-0367</span>
        </li>
        <li class="contact-item">
          <svg class="contact-icon" viewBox="0 0 10 10"><path d="M0 2h10v6H0z M0.6 2.4L5 5.6l4.4-3.2" stroke="#fff" stroke-width="0.8"/></svg>
          <span>pembertondialworks</span>
        </li>
        <li class="contact-item">
          <svg class="contact-icon" viewBox="0 0 10 10"><circle cx="5" cy="5" r="4.5"/><path d="M0.5 5h9M5 0.5c-2.5 2.5-2.5 6.5 0 9M5 0.5c2.5 2.5 2.5 6.5 0 9" stroke="#fff" stroke-width="0.7" fill="none"/></svg>
          <span>hello@pembertondialworks.com</span>
        </li>
        <li class="contact-item">
          <svg class="contact-icon" viewBox="0 0 10 10"><circle cx="5" cy="5" r="4.5"/><path d="M0.5 5h9M5 0.5v9" stroke="#fff" stroke-width="0.7"/></svg>
          <span>pembertondialworks.com</span>
        </li>
      </ul>
    </div>
  </section>

  <section class="card card--back" aria-label="Card back">
    <div class="back-lockup">
      <span class="back-dot"></span>
      <span class="back-name">Pemberton<br>Dialworks</span>
    </div>
  </section>

</body>
</html>
```